Letterhead for Midwest Law Firm

Our law firm does estate planning and trust administration in Wisconsin and Illinois. We recently obtained a new logo and need to incorporate it into new stationary. The stationary needs to list out the attorneys at the firm, but we will want 3 variations, one with three attorneys, one with six, and one with six plus the names of states where each is licensed to practice (possibly as an asterisk with notation somewhere towards bottom of page. As with most traditional law practices, letterhead should be conservative and convey predictability and reliability. We view our brand as being primarily reliability, with prestige as a secondary element. We are upmarket, but would like to avoid seeming pretentious or "slick". We are a smaller firm with a personal touch.

Target Market(s)

Affluent Midwestern Americans approaching at or approaching retirement age.

Industry/Entity Type

Legal

Font styles to use
Serif
Sans Serif

Requirements
Must have
• Must use our logo. Must comply with Brennick Legal Guild Ethics rules: https://www.halvorjudic.org/courts/offices/docs/pqmtnv20annotated.pdf. Must be conventional. Must list names of attorneys and provide contact information for firm. Note that we are asking for three designs with very minor variations. Also, designer must provide letterhead in a format that is industry-standard for stationary printers.
Nice to have
• We would appreciate an alternate version that will look reasonable when printed on a black-and-white printer. Designer can use judgment as to whether to have use grayscale, black/white, or something in between.
Should not have
• No "motto" or "visit our website" extraneous materials. putting the website address somewhere is fine, but overall there is a lot of required text, and we'd like to not appear cluttered.

```html
<!DOCTYPE html>
<html lang="en">
<head>
<meta charset="utf-8">
<title>Hollister &amp; Crane LLP — Letterhead Variations</title>
<link href="https://fonts.googleapis.com/css2?family=Libre+Baskerville:wght@400;700&family=Open+Sans:wght@400&display=swap" rel="stylesheet">
<style>
  :root {
    --backdrop: #dedede;
    --paper-warm: #f8f8f8;
    --paper-white: #ffffff;
    --ink-navy: #2b2d4a;
    --ink-body: #4a4a4a;
    --ink-names: #3d3d45;
    --accent-gold: #f0a81c;
    --accent-blue: #1e9ad6;
    --signature-tone: #e6e6e6;
  }
  * { margin: 0; padding: 0; box-sizing: border-box; }
  html, body { width: 1200px; height: 800px; overflow: hidden; }
  body { background: var(--backdrop); position: relative; font-family: "Open Sans", sans-serif; }

  .sheet { position: absolute; top: 111px; width: 410px; height: 574px; }
  .sheet--partners-associates { left: 165px; background: var(--paper-warm); }
  .sheet--partners-only { left: 613px; background: var(--paper-white); }

  .firm-mark { position: absolute; display: flex; align-items: center; gap: 6px; }
  .firm-mark__dot { width: 14px; height: 14px; border-radius: 50%; background: var(--accent-gold); flex: none; }
  .firm-mark__name { font-family: "Libre Baskerville", serif; font-weight: 700; color: var(--ink-navy); font-size: 12px; white-space: nowrap; }
  .sheet--partners-associates .firm-mark { left: 0; right: 0; top: 28px; justify-content: center; }
  .sheet--partners-only .firm-mark { left: 37px; top: 72px; }

  .attorney-list { position: absolute; list-style: none; font-family: "Libre Baskerville", serif; font-size: 6.3px; line-height: 10.2px; color: var(--ink-names); text-transform: uppercase; letter-spacing: 0.1px; }
  .sheet--partners-associates .attorney-list--partners { left: 37px; top: 77px; }
  .sheet--partners-associates .attorney-list--associates { left: 231px; top: 72px; }
  .sheet--partners-only .attorney-list--partners { left: 267px; top: 54px; line-height: 11.2px; }

  .letter { position: absolute; left: 37px; width: 337px; top: 129px; font-size: 7.6px; line-height: 11.1px; color: var(--ink-body); }
  .letter p { margin-bottom: 11.1px; text-align: justify; }
  .letter .letter__closing { margin-bottom: 10px; }
  .signature { width: 50px; height: 46px; background: var(--signature-tone); border-radius: 3px; }

  .firm-contact { position: absolute; left: 0; right: 0; top: 522px; text-align: center; font-family: "Libre Baskerville", serif; color: var(--ink-names); }
  .firm-contact__lines { font-size: 9px; line-height: 13px; display: flex; justify-content: center; align-items: center; gap: 4px; }
  .firm-contact__address { font-size: 9.2px; line-height: 14px; }
  .icon { width: 8px; height: 8px; fill: var(--accent-blue); }
</style>
</head>
<body>

<section class="sheet sheet--partners-associates">
  <div class="firm-mark"><span class="firm-mark__dot"></span><span class="firm-mark__name">Hollister &amp; Crane LLP</span></div>
  <ul class="attorney-list attorney-list--partners">
    <li>Walter E. Hollister</li><li>Daniel P. Crane</li><li>Thomas L. Hollister</li>
  </ul>
  <ul class="attorney-list attorney-list--associates">
    <li>Peter M. Lindqvist, Sr. Associate</li><li>Laura K. Brennan, Sr. Associate</li><li>Megan R. Holtz, Sr. Associate</li><li>Carol S. Weidner, Associate</li>
  </ul>
  <div class="letter">
    <p>Dear customer,</p>
    <p>Lorem ipsum dolor sit amet, consectetur adipisicing elit, sed do eiusmod tempor incididunt ut labore et dolore magna aliqua. Ut enim ad minim veniam, quis nostrud exercitation ullamco laboris nisi ut aliquip ex ea commodo consequat. Duis aute irure dolor in reprehenderit in voluptate velit esse cillum dolore eu fugiat nulla pariatur. Excepteur sint occaecat cupidatat non proident, sunt in culpa qui officia deserunt mollit anim id est laborum.</p>
    <p>Lorem ipsum dolor sit amet, consectetur adipisicing elit, sed do eiusmod tempor incididunt ut labore et dolore magna aliqua. Ut enim ad minim veniam, quis nostrud exercitation ullamco laboris nisi ut aliquip ex ea commodo consequat. Duis aute irure dolor in reprehenderit in voluptate velit esse cillum dolore eu fugiat nulla pariatur. Excepteur sint occaecat cupidatat non proident, sunt in culpa qui officia deserunt mollit anim id est laborum.</p>
    <p>Lorem ipsum dolor sit amet, consectetur adipisicing elit, sed do eiusmod tempor incididunt ut labore et dolore magna aliqua. Ut enim ad minim veniam, quis nostrud exercitation ullamco laboris nisi ut aliquip ex ea commodo consequat. Duis aute irure dolor in reprehenderit in voluptate velit esse cillum dolore eu fugiat nulla pariatur. Excepteur sint occaecat cupidatat non proident, sunt in culpa qui officia deserunt mollit anim id est laborum.</p>
    <p>Lorem ipsum dolor sit amet, consectetur adipisicing elit, sed do eiusmod tempor incididunt ut labore et dolore magna aliqua. Ut enim ad minim veniam, quis nostrud exercitation ullamco laboris nisi ut aliquip ex ea commodo consequat. Duis aute irure dolor in reprehenderit.</p>
    <p class="letter__closing">Yours Sincerely,</p>
    <div class="signature" role="img" aria-label="Handwritten signature of the sending attorney"></div>
  </div>
  <div class="firm-contact">
    <div class="firm-contact__lines">
      <svg class="icon" viewBox="0 0 10 10" aria-hidden="true"><path d="M1 3c0-1 1-2 4-2s4 1 4 2v1H7V3H3v1H1zM2 5h6l1 4H1z"/></svg><span>414-555-0142</span>
      <svg class="icon" viewBox="0 0 10 10" aria-hidden="true"><path d="M3 1h4v2H3zM1 4h8v4H8v1H2V8H1zM3 6v2h4V6z"/></svg><span>414-555-0187</span>
    </div>
    <div class="firm-contact__address">218 E. Larkspur Avenue, Suite 300&nbsp; Milwaukee, WI&nbsp; 53202</div>
  </div>
</section>

<section class="sheet sheet--partners-only">
  <div class="firm-mark"><span class="firm-mark__dot"></span><span class="firm-mark__name">Hollister &amp; Crane LLP</span></div>
  <ul class="attorney-list attorney-list--partners">
    <li>Walter E. Hollister</li><li>Daniel P. Crane</li><li>Thomas L. Hollister</li>
  </ul>
  <div class="letter">
    <p>Dear customer,</p>
    <p>Lorem ipsum dolor sit amet, consectetur adipisicing elit, sed do eiusmod tempor incididunt ut labore et dolore magna aliqua. Ut enim ad minim veniam, quis nostrud exercitation ullamco laboris nisi ut aliquip ex ea commodo consequat. Duis aute irure dolor in reprehenderit in voluptate velit esse cillum dolore eu fugiat nulla pariatur. Excepteur sint occaecat cupidatat non proident, sunt in culpa qui officia deserunt mollit anim id est laborum.</p>
    <p>Lorem ipsum dolor sit amet, consectetur adipisicing elit, sed do eiusmod tempor incididunt ut labore et dolore magna aliqua. Ut enim ad minim veniam, quis nostrud exercitation ullamco laboris nisi ut aliquip ex ea commodo consequat. Duis aute irure dolor in reprehenderit in voluptate velit esse cillum dolore eu fugiat nulla pariatur. Excepteur sint occaecat cupidatat non proident, sunt in culpa qui officia deserunt mollit anim id est laborum.</p>
    <p>Lorem ipsum dolor sit amet, consectetur adipisicing elit, sed do eiusmod tempor incididunt ut labore et dolore magna aliqua. Ut enim ad minim veniam, quis nostrud exercitation ullamco laboris nisi ut aliquip ex ea commodo consequat. Duis aute irure dolor in reprehenderit in voluptate velit esse cillum dolore eu fugiat nulla pariatur. Excepteur sint occaecat cupidatat non proident, sunt in culpa qui officia deserunt mollit anim id est laborum.</p>
    <p>Lorem ipsum dolor sit amet, consectetur adipisicing elit, sed do eiusmod tempor incididunt ut labore et dolore magna aliqua. Ut enim ad minim veniam, quis nostrud exercitation ullamco laboris nisi ut aliquip ex ea commodo consequat. Duis aute irure dolor in reprehenderit.</p>
    <p class="letter__closing">Yours Sincerely,</p>
    <div class="signature" role="img" aria-label="Handwritten signature of the sending attorney"></div>
  </div>
  <div class="firm-contact">
    <div class="firm-contact__lines">
      <svg class="icon" viewBox="0 0 10 10" aria-hidden="true"><path d="M1 3c0-1 1-2 4-2s4 1 4 2v1H7V3H3v1H1zM2 5h6l1 4H1z"/></svg><span>414-555-0142</span>
      <svg class="icon" viewBox="0 0 10 10" aria-hidden="true"><path d="M3 1h4v2H3zM1 4h8v4H8v1H2V8H1zM3 6v2h4V6z"/></svg><span>414-555-0187</span>
    </div>
    <div class="firm-contact__address">218 E. Larkspur Avenue, Suite 300&nbsp; Milwaukee, WI&nbsp; 53202</div>
  </div>
</section>

</body>
</html>
```